Landing Page and Logo for Auto-Blogging Platform

I created a platform that allows users to start a blog for their business, hobby, charity, etc. I need a landing page where users can learn about the platform, benefits of consistent blogging, SEO value, plans/pricing, etc. The landing page needs to have multiple call to action buttons encouraging the visitor to register/sign up for a free trial.

In addition to the landing page, I need a page for users to establish the settings for their blog. This page should be a fairly simple form, intended for the user to enter a few details to set up their blog:
1. Name of Blog
2. Up to 10 topics and/or keywords the blog should focus on
3. Theme: Color-scheme and logo upload for blog.

I have attached the specifications of the platform's functionality so you can better understand how it works, plans/pricing, etc.

I also need a logo for the business. The name of the platform is PostNook.

Target Market(s)

Website owners, bloggers, business owners

Industry/Entity Type

Technology, Internet, web design

Coding

Coded - Design and coding required

Number of Pages Required

2 page

Colors
0054AA
0677BA
7BADD7
CADEEF
E8F1F8
0094D4
00A9DD
6FCCEA
C7EBF8
E9F6FB

Requirements
Must have
• Eye-catching design but fairly light on content (keep it simple and brief.)
Nice to have
• Eye-catching yet simple design, clean and easy to understand what we are offering.
Should not have
• Too much “wordy” and confusing content.

```html
<!DOCTYPE html>
<html lang="en">
<head>
<meta charset="utf-8">
<title>PostNook – Auto-Blogging Platform</title>
<link href="https://fonts.googleapis.com/css2?family=Raleway:wght@400;500;600&display=swap" rel="stylesheet">
<style>
:root{
  --blue:#0054aa;
  --blue-mid:#0677ba;
  --blue-soft:#cadeef;
  --blue-pale:#e8f1f8;
  --ink:#1d1d1f;
  --text:#4a4a4a;
  --muted:#6b6b6b;
  --line:#e3e3e3;
  --hero-bg:#efedea;
  --band-bg:#f2f2f2;
  --white:#fff;
}
*{box-sizing:border-box;margin:0;padding:0}
html,body{width:1200px;height:3301px;overflow:hidden}
body{font-family:"Raleway",sans-serif;color:var(--text);background:var(--white);position:relative}
.abs{position:absolute}
a{color:inherit;text-decoration:none}

.topbar{top:0;left:0;width:1200px;height:40px;border-bottom:1px solid var(--line);text-align:center;font-size:14px;line-height:40px;color:var(--text)}
.topbar b{color:var(--blue);font-weight:500}

.nav{top:40px;left:0;width:1200px;height:78px;border-bottom:1px solid var(--line)}
.brand{display:flex;align-items:center;gap:12px;font-weight:600;color:var(--ink)}
.brand .mark{width:44px;height:44px;border-radius:50%;background:var(--blue)}
.nav .brand{position:absolute;left:112px;top:17px;font-size:25px}
.menu{position:absolute;right:160px;top:0;display:flex;gap:42px;font-size:16px;line-height:78px;color:var(--ink)}
.menu .active{color:var(--blue);font-weight:500;position:relative}
.menu .active::before{content:"";position:absolute;left:50%;top:18px;width:5px;height:5px;margin-left:-2px;border-radius:50%;background:var(--blue)}
.search{position:absolute;left:1072px;top:30px}

.hero{top:118px;left:0;width:1200px;height:497px;background:var(--hero-bg)}
.hero h1{position:absolute;left:112px;top:82px;font-size:43px;line-height:55px;font-weight:500;color:var(--ink)}
.hero h1 span{color:var(--blue)}
.hero p{position:absolute;left:112px;top:268px;width:450px;font-size:17px;line-height:26px}
.btn{display:inline-block;background:var(--blue);color:var(--white);border-radius:4px;font-size:15px;font-weight:500}
.hero .btn{position:absolute;left:112px;top:363px;width:226px;height:35px;line-height:35px;text-align:center}
.hero-photo{left:638px;top:10px;width:439px;height:500px;border-radius:220px 220px 0 0;background:linear-gradient(180deg,#e6ddd6,#cbbfb8 60%,#3f5f8a)}

.section-title{width:1200px;text-align:center;font-size:36px;font-weight:500;color:var(--blue)}
.section-lead{width:1200px;text-align:center;font-size:15px;line-height:23px}

.card{width:288px;height:296px;top:851px;background:var(--white);box-shadow:0 2px 10px rgba(0,0,0,.12);text-align:center}
.card svg{margin-top:24px}
.card h3{margin-top:24px;font-size:21px;font-weight:500;color:var(--ink)}
.card p{margin:12px auto 0;width:250px;font-size:12.5px;line-height:17px;color:var(--muted)}
.go{width:50px;height:50px;border-radius:50%;background:var(--blue);top:1127px}
.go svg{display:block;margin:13px}
.caption{top:1229px;width:1200px;text-align:center;font-size:17px;color:var(--ink)}
.caption u{color:var(--blue)}

.about{top:1337px;left:0;width:1200px;height:480px;background:var(--band-bg)}
.laptop{left:112px;top:83px;width:450px;height:311px;border-radius:14px;background:linear-gradient(160deg,#2b2d3a 0 62%,#d4d6da 62%)}
.about h2{position:absolute;left:600px;top:78px;font-size:36px;font-weight:500;color:var(--blue)}
.about .copy{position:absolute;left:600px;top:136px;width:489px;font-size:15px;line-height:23px;text-align:justify}
.about .btn{position:absolute;left:600px;top:349px;width:120px;height:35px;line-height:35px;text-align:center}

.plan{background:var(--white);border:1px solid #d9d9d9;border-radius:14px;text-align:center}
.plan h3{font-size:23px;font-weight:500;color:var(--ink)}
.plan .ico{margin:14px auto 0;width:122px;height:122px;border-radius:50%;background:var(--blue-pale);display:flex;align-items:center;justify-content:center}
.price{margin-top:22px;font-size:27px;font-weight:500;color:var(--ink)}
.price sup{font-size:11px;vertical-align:12px;margin-right:3px}
.price small{font-size:13px;margin-left:6px}
.get{display:block;margin:18px auto 0;width:196px;height:35px;line-height:33px;border:1px solid var(--blue-soft);border-radius:4px;font-size:15px;color:var(--blue-mid)}
.plan p{margin-top:20px;font-size:14px;line-height:20px;color:var(--text)}
.plan p span{display:block;font-size:16px;color:var(--blue)}

.methods{top:2550px;left:0;width:1200px;height:460px;background:var(--band-bg)}
.methods h2{position:absolute;left:112px;top:110px;font-size:36px;line-height:47px;font-weight:500;color:var(--blue)}
.methods ul{position:absolute;left:112px;top:262px;list-style:none;font-size:15px;line-height:21px}
.methods li{display:flex;gap:12px;margin-bottom:10px}
.methods li svg{flex:none;margin-top:2px}
.methods-photo{left:673px;top:65px;width:410px;height:395px;border-radius:200px 200px 0 0;background:linear-gradient(180deg,#d8d6d4,#7fc3d8 62%,#55595f)}

.footer{top:3010px;left:0;width:1200px;height:291px;background:#f7f8fa}
.footer .brand{position:absolute;left:112px;top:54px;font-size:32px}
.footer .brand .mark{width:56px;height:56px}
.footer .about-text{position:absolute;left:112px;top:130px;width:275px;font-size:14px;line-height:20px}
.col{position:absolute;top:58px}
.col h4{font-size:18px;font-weight:500;color:var(--blue);margin-bottom:8px}
.col a{display:block;font-size:14px;line-height:24px}
.pay{display:grid;grid-template-columns:auto auto auto;gap:12px 20px;font-size:17px;font-weight:600;color:var(--ink);margin-top:6px}
.footer .rule{position:absolute;left:112px;top:236px;width:976px;border-top:1px solid var(--blue-soft)}
.copy-line{position:absolute;top:250px;width:1200px;text-align:center;font-size:14px;color:var(--ink)}
</style>
</head>
<body>

<div class="abs topbar"><b>Lorem ipsum dolor</b> sit amet, consectetur adipiscing elit, sed do eiusmod</div>

<header class="abs nav">
  <div class="brand"><span class="mark"></span>PostNook</div>
  <nav class="menu">
    <a class="active">Home</a><a>About The Platform</a><a>Benefits</a><a>SEO Value</a><a>Pricing</a>
  </nav>
  <svg class="search" width="18" height="18" viewBox="0 0 18 18" fill="none" stroke="#1d1d1f" stroke-width="2"><circle cx="7.5" cy="7.5" r="5.5"/><path d="M12 12l4.5 4.5"/></svg>
</header>

<section class="abs hero">
  <h1><span>Trends &amp;<br>Techniques</span> You<br>Need To Try</h1>
  <p>The purpose of this platform is to allow anyone to start a blog and automate the process of creating content and posting it to the blog.</p>
  <a class="btn">Sign Up For A Free Trial</a>
  <div class="abs hero-photo" role="img" aria-label="Photo of a smiling man in glasses and a plaid shirt holding an open laptop"></div>
</section>

<h2 class="abs section-title" style="top:692px">Our Benefits</h2>
<p class="abs section-lead" style="top:753px">Lorem ipsum dolor sit amet, consectetur adipiscing elit, sed do eiusmod tempor incididunt ut<br>labore et dolore magna aliqua. Quis ipsum suspendisse ultrices gravida. Risus commodo viverra maecenas</p>

<div class="abs card" style="left:112px">
  <svg width="104" height="104" viewBox="0 0 104 104" fill="none" stroke="#0054aa" stroke-width="3"><rect x="4" y="4" width="76" height="96"/><path d="M88 12l12 4-10 84"/><path d="M42 16l14 6v12c0 8-6 12-14 16-8-4-14-8-14-16V22z"/><path d="M36 32l5 5 9-9"/><path d="M16 62l5 5 9-10M16 84l5 5 9-10M38 64h26M38 86h26"/></svg>
  <h3>Establishing Authority</h3>
  <p>Lorem ipsum dolor sit amet, consectetur adipiscing elit, sed do eiusmod tempor incididunt ut labore et dolore</p>
</div>
<div class="abs card" style="left:456px">
  <svg width="104" height="104" viewBox="0 0 104 104" fill="none" stroke="#0054aa" stroke-width="3"><rect x="2" y="4" width="100" height="96" rx="4"/><path d="M2 18h100"/><circle cx="12" cy="11" r="1.5"/><circle cx="20" cy="11" r="1.5"/><circle cx="28" cy="11" r="1.5"/><rect x="12" y="28" width="30" height="22"/><path d="M50 30h36M50 40h30M50 50h20M12 62h50M12 72h44M12 82h60"/><path d="M96 40L66 80l-4 12 12-4 30-40z"/></svg>
  <h3>Content Marketing</h3>
  <p>Lorem ipsum dolor sit amet, consectetur adipiscing elit, sed do eiusmod tempor incididunt ut labore et dolore</p>
</div>
<div class="abs card" style="left:800px">
  <svg width="104" height="104" viewBox="0 0 104 104" fill="none" stroke="#0054aa" stroke-width="3"><circle cx="64" cy="24" r="20"/><path d="M70 16h-9a4 4 0 000 8h6a4 4 0 010 8h-10M64 10v4M64 34v4"/><path d="M6 78l16-18c6-6 14-8 22-6l16 4h10a6 6 0 010 12H52M70 70l22-14a6 6 0 018 8L72 88H40"/><path d="M2 82l16 16 8-8-16-16z"/></svg>
  <h3>Cost-Effective</h3>
  <p>Lorem ipsum dolor sit amet, consectetur adipiscing elit, sed do eiusmod tempor incididunt ut labore et dolore</p>
</div>
<svg width="0" height="0" style="position:absolute"><defs><symbol id="arrow" viewBox="0 0 24 24"><path d="M3 12h17M13 5l7 7-7 7" fill="none" stroke="#fff" stroke-width="3" stroke-linecap="round" stroke-linejoin="round"/></symbol></defs></svg>
<a class="abs go" style="left:231px"><svg width="24" height="24"><use href="#arrow"/></svg></a>
<a class="abs go" style="left:575px"><svg width="24" height="24"><use href="#arrow"/></svg></a>
<a class="abs go" style="left:919px"><svg width="24" height="24"><use href="#arrow"/></svg></a>
<p class="abs caption">Lorem ipsum dolor <span style="color:var(--text)">sit amet, consectetur adipiscing elit,</span> <u>sed do eiusmod</u></p>

<section class="abs about">
  <div class="abs laptop" role="img" aria-label="Laptop showing the platform's analytics dashboard"></div>
  <h2>About The Platform</h2>
  <div class="copy">
    <p>There needs to be a super-admin panel where platform owner/administrator can see users, their activity, manage user access, etc.</p>
    <p>Each user will have a dashboard where they control their settings such as account information, billing, view blog posts, view blog post topics, etc. From this dashboard, the user can customize the “look and feel” of their blog including theme, hero banner, header, footer, logo, color scheme, etc.</p>
  </div>
  <a class="btn">Learn More</a>
</section>

<h2 class="abs section-title" style="top:1895px">Pricing</h2>
<p class="abs section-lead" style="top:1955px">Lorem ipsum dolor sit amet, consectetur adipiscing elit, sed do eiusmod tempor incididunt ut<br>labore et dolore magna aliqua. Quis ipsum suspendisse ultrices gravida. Risus commodo viverra maecenas</p>

<div class="abs plan" style="left:112px;top:2092px;width:294px;height:371px;padding-top:24px">
  <h3>Base</h3>
  <div class="ico"><svg width="70" height="70" viewBox="0 0 70 70" fill="none" stroke="#1d1d1f" stroke-width="3" stroke-linejoin="round"><path d="M35 6l14 7v14l-14 7-14-7V13zM21 13l14 7 14-7M35 20v14"/><path d="M14 30l21 11 21-11 10 5v16L35 66 4 51V35zM4 35l31 16 31-16M35 51v15"/></svg></div>
  <div class="price"><sup>$</sup>9.99<small>/mo</small></div>
  <a class="get">Get Started</a>
  <p>1 blog post (up to 2,000 words)<span>every month</span></p>
</div>
<div class="abs plan" style="left:445px;top:2064px;width:310px;height:399px;padding-top:24px;border:none;box-shadow:0 2px 12px rgba(0,0,0,.12)">
  <h3 style="color:var(--blue)">Premium</h3>
  <div class="ico" style="width:128px;height:128px"><svg width="70" height="70" viewBox="0 0 70 70" fill="none" stroke="#1d1d1f" stroke-width="3" stroke-linejoin="round"><path d="M64 6C46 6 32 16 22 36l12 12c20-10 30-24 30-42z"/><circle cx="46" cy="24" r="6"/><path d="M24 34H12L4 44h14M36 46v12l-10 8V52M18 52c-6 0-10 6-10 12 6 0 12-4 12-10"/></svg></div>
  <div class="price"><sup>$</sup>14.99<small>/mo</small></div>
  <a class="get" style="width:206px">Get Started</a>
  <p>1 blog post (up to 2,000 words)<span>every week</span></p>
</div>
<div class="abs plan" style="left:795px;top:2092px;width:293px;height:371px;padding-top:24px">
  <h3>Ultimate</h3>
  <div class="ico"><svg width="70" height="70" viewBox="0 0 70 70" fill="none" stroke="#1d1d1f" stroke-width="3" stroke-linejoin="round"><path d="M20 26h30l10 12-25 28L10 38zM10 38h50M27 26l8 40 8-40M20 26l15 12 15-12"/><path d="M35 4v12M22 8l4 10M48 8l-4 10"/></svg></div>
  <div class="price"><sup>$</sup>24.99<small>/mo</small></div>
  <a class="get">Get Started</a>
  <p>1 blog post (up to 2,000 words)<span>per day plus unlimited manual</span></p>
</div>

<section class="abs methods">
  <h2>The Blog Topics Can Be<br>Created Using Any<br>Of These Methods</h2>
  <ul>
    <li><svg width="16" height="16" viewBox="0 0 16 16" fill="none" stroke="#0054aa" stroke-width="1.6"><rect x="1" y="1" width="14" height="14" rx="2"/><path d="M4 8l3 3 5-6"/></svg>The user enters them into a table manually.</li>
    <li><svg width="16" height="16" viewBox="0 0 16 16" fill="none" stroke="#0054aa" stroke-width="1.6"><rect x="1" y="1" width="14" height="14" rx="2"/><path d="M4 8l3 3 5-6"/></svg>The user uploads a list of blog topics in CSV format.</li>
    <li><svg width="16" height="16" viewBox="0 0 16 16" fill="none" stroke="#0054aa" stroke-width="1.6"><rect x="1" y="1" width="14" height="14" rx="2"/><path d="M4 8l3 3 5-6"/></svg><span>AI can create the list of blog topics based on a prompt such as:<br>&nbsp;“ Provide a list of 52 blog topics for a handyman business’s blog.”</span></li>
  </ul>
  <div class="abs methods-photo" role="img" aria-label="Photo of a smiling woman with curly hair working on a laptop"></div>
</section>

<footer class="abs footer">
  <div class="brand"><span class="mark"></span>PostNook</div>
  <p class="about-text">The purpose of this platform is to allow anyone to start a blog and automate the process of creating content and posting it to the blog.</p>
  <div class="col" style="left:459px"><h4>Quick Links</h4><a>Home</a><a>About The Platform</a><a>Benefits</a><a>Pricing</a><a>SEO Values</a></div>
  <div class="col" style="left:668px"><h4>Other Links</h4><a>FAQs</a><a>Help Center</a><a>Terms &amp; Conditions</a><a>Privacy Policy</a><a>Sitemap</a></div>
  <div class="col" style="left:875px"><h4>Payment</h4>
    <div class="pay"><span>Strand</span><span>Paywell</span><span>OrchardPay</span><span>GlyphPay</span><span>RiverPay</span></div>
  </div>
  <div class="rule"></div>
  <p class="copy-line">Copyright © 2024 PostNook. All rights reserved.</p>
</footer>

</body>
</html>
```